Neuropsychology Private Practice - Advertising Materials

We need a postcard (probably multiple) to let other doctors in the area know about our private practice, what we have to offer, and where we are at. This would be something to hand out to Dr.'s and also leave in their waiting rooms. Much more through information about the types of services offered at the practice and what a neuropsychological assessment is are included in the supplemental (attacked documents). Also there is a digital copy of the practices logo

Target Market(s)

Medical Professionals (MD's, Nurse Practitioners, OT/PT).

Industry/Entity Type

Advertising

Font styles to use
Serif
Sans Serif

Requirements
Must have
• Practice Logo, Contact Information, Provider Information
Nice to have
• Images, Pictures, something to catch a person's eye

```html
<!DOCTYPE html>
<html lang="en">
<head>
<meta charset="utf-8">
<title>Lakeside Neuro Care – Referral Flyer</title>
<link href="https://fonts.googleapis.com/css2?family=Arimo:ital,wght@0,400;0,700;1,400&display=swap" rel="stylesheet">
<style>
  :root {
    --page-bg: #e9ecef;
    --navy: #1f2a9c;
    --ink: #1b3f8f;
    --sky-light: #dff1fa;
    --sky: #8fcdf0;
    --blue: #1d74c8;
    --blue-deep: #0b3f8c;
    --white: #ffffff;
  }
  * { box-sizing: border-box; margin: 0; padding: 0; }
  html, body { width: 1200px; height: 796px; overflow: hidden; }
  body { background: var(--page-bg); font-family: "Arimo", Arial, sans-serif; }

  .flyer {
    position: absolute; left: 220px; top: 18px; width: 760px; height: 760px;
    background: linear-gradient(180deg, var(--white) 0%, var(--sky-light) 55%, var(--sky) 100%);
    overflow: hidden; box-shadow: 0 6px 18px rgba(0,0,0,.18);
  }
  .backdrop { position: absolute; left: 0; top: 0; width: 760px; height: 760px; }

  .brand { position: absolute; left: 440px; top: 40px; display: flex; align-items: center; gap: 12px; white-space: nowrap; }
  .brand-dot { width: 38px; height: 38px; border-radius: 50%; background: var(--navy); flex: none; }
  .brand-name { font-size: 26px; font-weight: 700; color: var(--navy); line-height: 1; }
  .tagline { position: absolute; left: 440px; top: 90px; font-size: 11px; font-style: italic; color: var(--navy); white-space: nowrap; }

  .details { position: absolute; left: 440px; top: 135px; width: 295px; color: var(--ink); font-size: 12.5px; line-height: 1.3; }
  .details h2 { font-size: 12.5px; font-weight: 700; color: var(--navy); text-transform: uppercase; margin-bottom: 2px; }
  .details p { margin-bottom: 12px; }
  .details ol { padding-left: 18px; margin-bottom: 14px; }

  .photo {
    position: absolute; left: 40px; top: 340px; width: 340px; height: 340px; border-radius: 50%;
    background: radial-gradient(circle at 55% 60%, #cfe6f7 0%, #8fb9df 45%, #4d7fb4 100%);
    border: 6px solid rgba(255,255,255,.9);
  }

  .address { position: absolute; left: 440px; top: 650px; width: 300px; color: var(--ink); font-size: 12px; line-height: 1.4; }
  .address h2 { font-size: 12.5px; font-weight: 700; color: var(--navy); text-transform: uppercase; }
  .address .phones { font-weight: 700; color: var(--blue); }
</style>
</head>
<body>
  <main class="flyer">
    <svg class="backdrop" viewBox="0 0 760 760" role="img" aria-label="Blue technology backdrop with glass bubbles and light rings">
      <defs>
        <linearGradient id="tech-blue" x1="0" y1="0" x2="1" y2="1">
          <stop offset="0" stop-color="#3d9be0"/>
          <stop offset="1" stop-color="#0b3f8c"/>
        </linearGradient>
      </defs>
      <path d="M0 300 C160 270 340 320 405 440 C440 540 410 660 360 760 L0 760 Z" fill="url(#tech-blue)"/>
      <circle cx="210" cy="510" r="186" fill="none" stroke="#ffffff" stroke-opacity=".7" stroke-width="6"/>
      <circle cx="210" cy="510" r="202" fill="none" stroke="#2a6fc0" stroke-width="8"/>
      <circle cx="60" cy="720" r="22" fill="#1d74c8" fill-opacity=".7"/>
      <circle cx="300" cy="735" r="14" fill="#1d74c8" fill-opacity=".6"/>
    </svg>

    <div class="brand">
      <span class="brand-dot"></span>
      <span class="brand-name">Lakeside Neuro Care</span>
    </div>
    <div class="tagline">Professional understanding, practical solutions.</div>

    <section class="details">
      <h2>Overview of practice:</h2>
      <p>A multi-disciplinary outpatient behavioral health practice providing comprehensive evaluation, medication management, and ongoing therapy for both pediatric and adult patients. Flexible Scheduling, including after school appointments.</p>
      <ol>
        <li>Most Pediatric Medicaid plans accepted</li>
        <li>Many private insurance plans accepted (Adult &amp; Pediatric)</li>
        <li>Reasonable self-pay rates</li>
      </ol>
      <h2>Specific services offered:</h2>
      <ol>
        <li>Neuropsychological Assessment</li>
        <li>Psychological Assessment</li>
        <li>Medication Management</li>
        <li>Individual Therapy</li>
        <li>Diagnostic Services</li>
      </ol>
    </section>

    <div class="photo" role="img" aria-label="Clinician in a white coat studying a glowing holographic brain"></div>

    <section class="address">
      <h2>Practice address :</h2>
      <div>2210 Harbor Lane Suite B, Riverton, LA 70999</div>
      <div class="phones">Tel : 555-014-2600 · Fax : 555-014-2601</div>
    </section>
  </main>
</body>
</html>
```